Brisbane IT support business needs our first business card

Hello we are a Brisbane based Information Technology company providing support and services to small and medium sized businesses. We provide a range of services and solutions.

The business name is Wattlebrook Network Computing Services, or WNCS for short.

I am looking for a business card that looks professional (don't we all want that), but most importantly, it most utilize the colours in the logo attached.

Reason: Launched late, extending so people have enough time to actually submit something.

Target Market(s)

Other business owners seeking our IT services, and also home users.

Industry/Entity Type

Business

Requirements
Must have
• Please only use the blue/orange colours in logo attached

```html
<!DOCTYPE html>
<html lang="en">
<head>
<meta charset="utf-8">
<title>WNCS Business Card</title>
<link rel="stylesheet" href="https://fonts.googleapis.com/css2?family=Roboto:wght@400;500;700&display=swap">
<style>
  :root {
    --navy: #0f3a63;
    --orange: #f07a1a;
    --white: #ffffff;
    --page: #e4e7eb;
    --soft: #eef3f5;
  }
  * { box-sizing: border-box; margin: 0; padding: 0; }
  html, body { width: 1200px; height: 960px; overflow: hidden; }
  body {
    background: var(--page);
    font-family: "Roboto", Arial, sans-serif;
    position: relative;
  }
  .card {
    position: absolute;
    width: 640px;
    height: 366px;
    border-radius: 16px;
    overflow: hidden;
    background: var(--white);
    box-shadow: 0 10px 28px rgba(15, 58, 99, 0.18);
  }
  .card--front { left: 120px; top: 70px; }
  .card--back { left: 440px; top: 520px; }

  /* Front */
  .front__mark {
    position: absolute;
    left: 50%;
    top: 150px;
    transform: translate(-50%, -50%);
    display: flex;
    align-items: center;
    gap: 18px;
  }
  .mark-dot {
    width: 72px; height: 72px;
    border-radius: 50%;
    background: var(--navy);
  }
  .mark-name {
    font-weight: 700;
    font-size: 60px;
    line-height: 1;
    color: var(--orange);
    letter-spacing: 1px;
  }
  .front__band {
    position: absolute;
    left: 0; right: 0; bottom: 0;
    height: 48px;
    background: var(--navy);
    display: flex;
    align-items: center;
    justify-content: center;
  }
  .front__web {
    color: var(--white);
    font-size: 15px;
    letter-spacing: 0.5px;
  }

  /* Back */
  .back__top {
    position: absolute;
    left: 0; right: 0; top: 0;
    height: 140px;
    background: var(--white);
  }
  .back__brand {
    position: absolute;
    left: 70px;
    top: 34px;
    display: flex;
    align-items: center;
    gap: 18px;
  }
  .back__brand .mark-dot { width: 76px; height: 76px; }
  .back__divider {
    width: 2px; height: 64px;
    background: var(--orange);
  }
  .back__names { display: flex; flex-direction: column; gap: 4px; }
  .back__names .mark-name { font-size: 50px; }
  .back__fullname {
    font-weight: 700;
    font-size: 9.5px;
    line-height: 1.2;
    color: var(--navy);
    text-transform: uppercase;
    width: 170px;
  }
  .back__stripe {
    position: absolute;
    left: 0; right: 0; top: 140px;
    height: 38px;
    background: var(--orange);
  }
  .back__person {
    position: absolute;
    left: 248px;
    top: 140px;
    height: 38px;
    display: flex;
    align-items: center;
    color: var(--white);
    font-size: 24px;
    font-weight: 500;
  }
  .back__body {
    position: absolute;
    left: 0; right: 0; top: 178px; bottom: 0;
    background: var(--navy);
    color: var(--white);
  }
  .back__role {
    position: absolute;
    left: 248px; top: 10px;
    font-size: 16px;
  }
  .back__contact {
    position: absolute;
    left: 248px; top: 56px;
    list-style: none;
    font-size: 15px;
    line-height: 1.65;
  }
</style>
</head>
<body>
  <section class="card card--front" aria-label="Card front">
    <div class="front__mark">
      <span class="mark-dot"></span>
      <span class="mark-name">WNCS</span>
    </div>
    <div class="front__band">
      <span class="front__web">www.yourwebsite.com</span>
    </div>
  </section>

  <section class="card card--back" aria-label="Card back">
    <div class="back__top">
      <div class="back__brand">
        <span class="mark-dot"></span>
        <span class="back__divider"></span>
        <div class="back__names">
          <span class="mark-name">WNCS</span>
          <span class="back__fullname">Wattlebrook Network Computing Services</span>
        </div>
      </div>
    </div>
    <div class="back__stripe"></div>
    <div class="back__person">Employee Name</div>
    <div class="back__body">
      <p class="back__role">Managing Director</p>
      <ul class="back__contact">
        <li>0012 3456 789</li>
        <li>info@youremail.com</li>
        <li>www.yourwebsite.com</li>
        <li>Your Adress Inc 2nd Lane Ave Edison, NJ 00000</li>
      </ul>
    </div>
  </section>
</body>
</html>
```